Lease-A-Goose's web page

I need a web page(s) to show and promote my business of renting chickens. We provide seasonal rentals in the United States of a layer hen package for people who would like to try raising their own chickens. The package includes two hens, coop, attached run, feeder, waterer, and food. I would like interested people to be able to fill out a form so that I can have partners contact them to set up a delivery in their area. Our service is very popular with urban and suburban families.

Target Market(s)

Urban foodies.
Families.
People interested in Organic Foods.
People concerned with where their food comes from and how it is grown/prepared.
People interested in Urban Farming.

Industry/Entity Type

Business

Requirements
Must have
• A way for me to see rental interest based on zip code.
• A contact form including zip code, e-mail, and optional phone number.
• Our Logo. (Please contact if you are unable to use the file I provided.)
Nice to have
• A guest book for former renters that we can vet before posting.

```html
<!DOCTYPE html>
<html lang="en">
<head>
<meta charset="utf-8">
<title>Lease-A-Goose</title>
<link href="https://fonts.googleapis.com/css2?family=Source+Sans+3:wght@400;600&display=swap" rel="stylesheet">
<style>
:root{
  --cream:#f3f2e0;
  --cream-light:#fbfbf1;
  --red:#b3241c;
  --red-dark:#8e1a14;
  --olive:#86a128;
  --olive-dark:#5f7a14;
  --orange:#c9890a;
  --text:#4a4a42;
  --nav-text:#8a5a0a;
  --line:#dcdcd0;
  --field:#ffffff;
  --field-border:#d7d7cc;
  --sky:#7fd3ee;
  --sky-light:#b9ecfa;
  --navy:#1d4d6b;
}
*{margin:0;padding:0;box-sizing:border-box}
html,body{width:972px;height:1200px;overflow:hidden}
body{
  position:relative;
  font-family:"Source Sans 3",sans-serif;
  color:var(--text);
  background:radial-gradient(ellipse 420px 260px at 486px 40px,var(--cream-light),var(--cream) 70%),var(--cream);
}
.abs{position:absolute}
.social{left:82px;top:61px;display:flex;gap:8px}
.share{display:flex;align-items:center;gap:3px}
.share .btn{width:38px;height:16px;border:1px solid #c9cdd8;border-radius:2px;background:#eef0f5}
.share .count{font-size:10px;border:1px solid #ccc;background:#fff;padding:0 3px;height:16px;line-height:14px}
.call{right:82px;top:56px;font-size:19px;color:var(--olive)}
.call b{font-weight:400;color:var(--red)}
.nav{left:80px;top:102px;width:812px;height:36px}
.nav ul{position:absolute;top:0;left:0;width:100%;height:36px;list-style:none;font-size:13px;font-weight:600;color:var(--nav-text)}
.nav li{position:absolute;top:11px}
.nav li.active{color:var(--red)}
.panel{left:83px;top:139px;width:806px;height:985px;background:#fff;border-radius:3px}
.brand{left:400px;top:14px;width:172px;height:150px;z-index:5}
.brand .plate{position:absolute;left:17px;top:0;width:138px;height:138px;border-radius:50%;background:#f4f1df;border:4px solid #fff}
.brand .name{position:absolute;left:0;top:100px;width:172px;text-align:center;font-size:22px;line-height:26px;font-weight:600;color:var(--red)}
.hero{left:89px;top:149px;width:794px;height:308px;border-radius:4px;
  background:linear-gradient(100deg,#6f9a1e 0%,#8fb83a 40%,#b89a55 65%,#9bbd4a 100%)}
.hero h1{position:absolute;left:26px;top:76px;font-size:22px;font-weight:600;line-height:29px;color:#fff;text-shadow:0 1px 2px rgba(0,0,0,.35)}
.hero ul{position:absolute;left:26px;top:145px;width:300px;list-style:none;display:grid;grid-template-columns:158px 140px;row-gap:8px;font-size:18.5px;font-weight:600;color:#fff;text-shadow:0 1px 2px rgba(0,0,0,.35)}
.hero li{display:flex;align-items:center;gap:10px;line-height:22px}
.hero .next{position:absolute;left:742px;top:136px;width:34px;height:34px;border-radius:50%;background:rgba(255,255,240,.75)}
h2{font-weight:400}
.welcome{left:92px;top:478px;font-size:22px;color:var(--red)}
p{font-size:12px;line-height:18.6px}
.intro{left:92px;top:519px;width:542px}
.photo{border:2px solid #e3e3da;border-radius:2px}
.hen-photo{left:93px;top:592px;width:221px;height:128px;background:linear-gradient(110deg,#cfc7b6,#8a5a2a 55%,#b9b3a8)}
.detail{left:333px;top:587px;width:301px}
.detail p{font-size:11.4px;letter-spacing:-0.15px;text-align:justify}
.more{display:block;margin-top:8px;font-size:13px;color:var(--orange)}
.rule{height:1px;background:var(--line)}
.gallery-title{left:92px;top:765px;font-size:19px;color:var(--olive)}
.gallery-arrows{left:612px;top:772px}
.g1{left:93px;top:806px;width:170px;height:107px;background:linear-gradient(120deg,#b9a27a,#8a4f22 55%,#d7d0c0)}
.g2{left:278px;top:806px;width:170px;height:107px;background:linear-gradient(120deg,#8d7052,#6b5238 50%,#a98a66)}
.g3{left:462px;top:806px;width:170px;height:107px;background:linear-gradient(120deg,#587a2a,#d9d6cc 55%,#6e8b36)}
.form-box{left:663px;top:482px;width:218px;height:342px;border:1px solid #e2e2d8;border-radius:3px;background:linear-gradient(#fff,#f7f7f2)}
.form-ribbon{left:656px;top:489px;width:220px;height:36px}
.form-ribbon span{position:absolute;left:21px;top:6px;font-size:18.5px;font-weight:600;color:#f8e3a8}
.field{left:673px;width:198px;height:35px;background:var(--field);border:1px solid var(--field-border);border-bottom-width:4px;border-radius:3px;font-size:12px;color:#8a8a82;padding:10px 14px}
.submit{left:809px;top:782px;width:62px;height:29px;border-radius:3px;background:linear-gradient(var(--olive),var(--olive-dark));color:#fff;font-size:13px;font-weight:600;text-align:center;line-height:29px}
.testimonials{left:663px;top:841px;width:218px;height:72px;border-radius:3px;border:1px solid #6fc6e2;background:linear-gradient(135deg,var(--sky-light),var(--sky))}
.testimonials span{position:absolute;left:59px;top:14px;font-size:16.5px;font-weight:600;line-height:22px;color:var(--navy)}
.blog-title{left:99px;top:958px;font-size:19px;color:var(--olive)}
.blog-photo{left:101px;top:998px;width:214px;height:114px;background:linear-gradient(90deg,#4b7a3a,#c2a48a 35%,#3f78b8 60%,#e9e4da)}
.post-title{left:334px;top:993px;font-size:14px;font-weight:400;color:var(--olive-dark)}
.post-date{left:334px;top:1013px;font-size:12px}
.post-body{left:334px;top:1041px;width:539px;text-align:justify}
.footer-links{left:83px;top:1141px;font-size:11px;word-spacing:2px}
.copyright{left:83px;top:1167px;font-size:11px;word-spacing:2px}
.footer-social{left:843px;top:1152px;display:flex;gap:5px}
.footer-social i{display:block;width:20px;height:20px;border-radius:3px}
</style>
</head>
<body>

<div class="abs social">
  <div class="share"><div class="btn"></div><span class="count">3k</span></div>
  <div class="share"><div class="btn"></div><span class="count">316</span></div>
</div>
<div class="abs call">Call us : <b>555 014 2290</b></div>

<nav class="abs nav">
  <svg width="812" height="36" viewBox="0 0 812 36" style="position:absolute;left:0;top:0">
    <defs>
      <linearGradient id="navfill" x1="0" y1="0" x2="0" y2="1">
        <stop offset="0" stop-color="#ffd84a"/><stop offset="1" stop-color="#f5a816"/>
      </linearGradient>
    </defs>
    <polygon points="0,0 812,0 790,18 812,36 0,36 22,18" fill="url(#navfill)"/>
    <polygon points="0,0 14,0 14,10" fill="#d98a10"/>
    <polygon points="812,0 798,0 798,10" fill="#d98a10"/>
  </svg>
  <ul>
    <li class="active" style="left:43px">HOME</li>
    <li style="left:119px">ABOUT US</li>
    <li style="left:216px">OUR SERVICE</li>
    <li style="left:531px">PRICING</li>
    <li style="left:618px">BLOG</li>
    <li style="left:689px">CONTACT US</li>
  </ul>
</nav>

<div class="abs panel"></div>

<div class="abs brand">
  <div class="plate"></div>
  <div class="name">Lease-A-Goose</div>
</div>

<section class="abs hero" role="img" aria-label="Photo of a brown hen walking on green grass">
  <h1>Donec volutpat, nunc eget auctor<br>convallis, felis bibendum.</h1>
  <ul>
    <li><svg width="12" height="10" viewBox="0 0 12 10"><path d="M1 5l3 3 7-7" fill="none" stroke="#fff" stroke-width="2"/></svg>Two hens</li>
    <li><svg width="12" height="10" viewBox="0 0 12 10"><path d="M1 5l3 3 7-7" fill="none" stroke="#fff" stroke-width="2"/></svg>Feeder</li>
    <li><svg width="12" height="10" viewBox="0 0 12 10"><path d="M1 5l3 3 7-7" fill="none" stroke="#fff" stroke-width="2"/></svg>Coop</li>
    <li><svg width="12" height="10" viewBox="0 0 12 10"><path d="M1 5l3 3 7-7" fill="none" stroke="#fff" stroke-width="2"/></svg>Waterer</li>
    <li><svg width="12" height="10" viewBox="0 0 12 10"><path d="M1 5l3 3 7-7" fill="none" stroke="#fff" stroke-width="2"/></svg>Attached run</li>
    <li><svg width="12" height="10" viewBox="0 0 12 10"><path d="M1 5l3 3 7-7" fill="none" stroke="#fff" stroke-width="2"/></svg>Food</li>
  </ul>
  <div class="next"><svg width="34" height="34" viewBox="0 0 34 34"><path d="M14 11l6 6-6 6" fill="none" stroke="#7a8a5a" stroke-width="1.6"/></svg></div>
</section>

<h2 class="abs welcome">Welcome to LeaseAGoose</h2>
<p class="abs intro">Donec ac gravida sapien. Aenean dolor elit, blandit vitae blandit non, commodo ac lorem. Donec nec adipiscing dolor, vel posuere metus. Mauris accumsan leo posuere, lobortis augue at, luctus tortor. Proin gravida nisi quis posuere tristique. Sed sed nulla euismod urna porta interdum nec vel ante.</p>
<div class="abs photo hen-photo" role="img" aria-label="Photo of a mother hen with her chicks"></div>
<div class="abs detail">
  <p>Donec ac gravida sapien. Aenean dolor elit, blandit vitae blandit non, commodo ac lorem. Donec nec adipiscing dolor, vel posuere metus. Mauris accumsan leo posuere, lobortis augue at, luctus tortor. Proin gravida nisi quis posuere tristique. Sed sed nulla euismod urna porta interdum nec vel ante. Nulla nibh tortor, posuere nec nisi sed.</p>
  <a class="more">Know More</a>
</div>
<div class="abs rule" style="left:89px;top:745px;width:546px"></div>

<h2 class="abs gallery-title">Our Gallery</h2>
<svg class="abs gallery-arrows" width="24" height="10" viewBox="0 0 24 10"><path d="M8 1L1 5l7 4z" fill="#aaa"/><path d="M16 1l7 4-7 4z" fill="#999"/></svg>
<div class="abs photo g1" role="img" aria-label="Photo of a hen with chicks by a fence"></div>
<div class="abs photo g2" role="img" aria-label="Photo of a hen and chicks on bare earth"></div>
<div class="abs photo g3" role="img" aria-label="Photo of a white hen with chicks on grass"></div>

<aside>
  <div class="abs form-box"></div>
  <div class="abs form-ribbon">
    <svg width="220" height="44" viewBox="0 0 220 44" style="position:absolute;left:0;top:0">
      <defs><linearGradient id="rib" x1="0" y1="0" x2="0" y2="1"><stop offset="0" stop-color="#c8352a"/><stop offset="1" stop-color="#a41f18"/></linearGradient></defs>
      <polygon points="0,0 220,0 200,18 220,36 0,36" fill="url(#rib)"/>
      <polygon points="0,36 8,36 8,42" fill="#6e140f"/>
    </svg>
    <span>Contact Form</span>
  </div>
  <div class="abs field" style="top:541px">Name</div>
  <div class="abs field" style="top:583px">Phone</div>
  <div class="abs field" style="top:625px">E-mail</div>
  <div class="abs field" style="top:667px;height:102px">Address</div>
  <div class="abs submit">SUBMIT</div>
  <div class="abs testimonials">
    <svg width="30" height="24" viewBox="0 0 30 24" style="position:absolute;left:24px;top:24px"><ellipse cx="15" cy="11" rx="13" ry="9" fill="#eaf8fd"/><path d="M8 18l-2 5 7-4z" fill="#eaf8fd"/></svg>
    <span>View Our Customers<br>Testimonials</span>
  </div>
</aside>

<div class="abs rule" style="left:89px;top:948px;width:790px"></div>
<h2 class="abs blog-title">Our Blog</h2>
<div class="abs blog-photo" role="img" aria-label="Photo of two speckled hens side by side"></div>
<h3 class="abs post-title">Cras placerat eleifend magna, ut venenatis nibh</h3>
<div class="abs post-date">October 16, 2013</div>
<p class="abs post-body">Aenean dolor elit, blandit vitae blandit non, commodo ac lorem. Donec nec adipiscing dolor, vel posuere metus. Mauris accumsan leo posuere, lobortis augue at, luctus tortor. Proin gravida nisi quis posuere tristique. Nunc non interdum nunc. Ut neque tortor, vehicula eget malesuada placerat, luctus at mi. Phasellus ac urna eros. Sed hendrerit pellentesque justo non cursus.</p>

<footer>
  <div class="abs footer-links">Home &nbsp;|&nbsp; About us &nbsp;|&nbsp; Our Servic &nbsp;|&nbsp; Pricing &nbsp;|&nbsp; Blog &nbsp;|&nbsp; Contact us</div>
  <div class="abs copyright">Copyright © 2013 &nbsp;LeaseAGoose. &nbsp;All rights reserved.</div>
  <div class="abs footer-social"><i style="background:#3b5998"></i><i style="background:#3fb4e8"></i></div>
</footer>

</body>
</html>
```